Business Card Design for Tax Accounting Company

I need design files that can be edited to add new professional designations onto the end of my name once complete. I need design files that can be edited for new employees. I also need the design files to be able to upload into PrintHollow for new orders. I've attached multiple logo files with varying file extensions to help with the design.
Please include the following contact information:
Marcus Tenley, CFP®, EA, CTC, CEPA
Founder & CEO
C (480) 517.3082
F (623) 391.7258
418 W Larkspur Ave
Quarry Flats, AZ 85990
Updates
I need the business card to include the following contact info:
C: (480)517.3082
F: (623) 391.7258
mt@QuarrystoneLedgerworks.com
www.MarcusRTenley.com
Address to be included is
418 W Larkspur Ave
Quarry Flats, AZ 85990
Business Cards are double sided
Target Market(s)
Business owners $1M+ annual revenue, especially for the construction and technology industries
Industry/Entity Type
Accounting & Tax
Contact Information for Business Card
Contact information and logo
Look and feel

```html
<!DOCTYPE html>
<html lang="en">
<head>
<meta charset="utf-8">
<title>Quarrystone Ledgerworks Inc. – Business Card</title>
<link rel="stylesheet" href="https://fonts.googleapis.com/css2?family=Lora:wght@400;700&display=swap">
<style>
  :root {
    --stage: #3a3a3c;
    --orange: #c95a22;
    --orange-light: #d4662a;
    --navy: #1f2d5c;
    --grey-text: #6b6b6b;
    --card-white: #f6f6f6;
  }
  * { margin: 0; padding: 0; box-sizing: border-box; }
  html, body {
    width: 1200px; height: 900px; overflow: hidden;
    background: var(--stage);
    font-family: "Lora", Georgia, serif;
  }
  .stage { position: relative; width: 1200px; height: 900px; }

  .card {
    position: absolute; left: 280px; width: 640px; height: 366px;
    border-radius: 36px; overflow: hidden;
    box-shadow: 0 12px 30px rgba(0,0,0,.45);
  }
  .card--front { top: 50px; background: linear-gradient(135deg, var(--orange), var(--orange-light)); }
  .card--back { top: 470px; background: var(--card-white); }

  /* brand lockup */
  .brand { display: flex; align-items: center; gap: 12px; white-space: nowrap; }
  .brand__dot { border-radius: 50%; background: var(--navy); flex: none; }
  .brand__name { color: var(--navy); font-weight: 700; line-height: 1.1; white-space: nowrap; }
  .brand__tagline { color: var(--navy); white-space: nowrap; }

  .front-lockup {
    position: absolute; left: 50%; top: 50%; transform: translate(-50%, -50%);
    display: flex; flex-direction: column; align-items: center;
  }
  .front-lockup .brand__dot { width: 40px; height: 40px; }
  .front-lockup .brand__name { font-size: 34px; }
  .front-lockup .brand__tagline { font-size: 13px; margin-top: 10px; }

  .back-lockup { position: absolute; left: 34px; top: 70px; }
  .back-lockup .brand__dot { width: 30px; height: 30px; }
  .back-lockup .brand__name { font-size: 22px; }
  .back-lockup .brand__tagline { font-size: 11px; margin-top: 6px; }

  .person {
    position: absolute; left: 34px; top: 200px; width: 224px; text-align: right;
    white-space: nowrap;
  }
  .person__creds { color: var(--grey-text); font-size: 15px; }
  .person__name { color: var(--navy); font-size: 20px; letter-spacing: .5px; margin-top: 4px; }

  .divider {
    position: absolute; left: 276px; top: 160px; width: 2px; height: 160px;
    background: var(--orange);
  }
  .contact {
    position: absolute; left: 296px; top: 160px; list-style: none;
    color: var(--navy); font-size: 15px; white-space: nowrap;
  }
  .contact li { display: flex; align-items: center; gap: 10px; height: 32px; }
  .contact svg { width: 15px; height: 15px; fill: var(--navy); flex: none; }
</style>
</head>
<body>
<main class="stage">

  <section class="card card--front">
    <div class="front-lockup">
      <div class="brand">
        <span class="brand__dot"></span>
        <span class="brand__name">Quarrystone Ledgerworks Inc.</span>
      </div>
      <p class="brand__tagline">Clear Questions. Steady Answers. Higher Ground.</p>
    </div>
  </section>

  <section class="card card--back">
    <div class="back-lockup">
      <div class="brand">
        <span class="brand__dot"></span>
        <span class="brand__name">Quarrystone Ledgerworks Inc.</span>
      </div>
      <p class="brand__tagline">Clear Questions. Steady Answers. Higher Ground.</p>
    </div>

    <div class="person">
      <p class="person__creds">CFP®, EA, CTC, CEPA</p>
      <p class="person__name">MARCUS TENLEY</p>
    </div>

    <div class="divider"></div>

    <ul class="contact">
      <li>
        <svg viewBox="0 0 16 16" aria-hidden="true"><path d="M3 1h3l1.5 4-2 1.2a9 9 0 0 0 4.3 4.3L11 8.5l4 1.5v3a2 2 0 0 1-2 2A12 12 0 0 1 1 3a2 2 0 0 1 2-2z"/></svg>
        (480)517.3082
      </li>
      <li>
        <svg viewBox="0 0 16 16" aria-hidden="true"><path d="M4 1h7v4H4zM2 6h12v7h-2v2H4v-2H2zm3 5v3h6v-3z"/></svg>
        (623) 391.7258
      </li>
      <li>
        <svg viewBox="0 0 16 16" aria-hidden="true"><path d="M8 1a7 7 0 1 0 0 14A7 7 0 0 0 8 1zm0 1.5c.8 1 1.4 2.6 1.5 4.5h-3C6.6 5.1 7.2 3.5 8 2.5zM2.6 9h2.4c.1 1.6.5 3 1.1 4A5.5 5.5 0 0 1 2.6 9zm0-2a5.5 5.5 0 0 1 3.5-4c-.6 1-1 2.4-1.1 4zm8.4 0c-.1-1.6-.5-3-1.1-4a5.5 5.5 0 0 1 3.5 4zm0 2h2.4a5.5 5.5 0 0 1-3.5 4c.6-1 1-2.4 1.1-4zM6.5 9h3c-.1 1.9-.7 3.5-1.5 4.5-.8-1-1.4-2.6-1.5-4.5z"/></svg>
        www.MarcusRTenley.com
      </li>
      <li>
        <svg viewBox="0 0 16 16" aria-hidden="true"><path d="M1 3h14v10H1zm1.5 1.5L8 9l5.5-4.5z" fill-rule="evenodd"/></svg>
        mt@QuarrystoneLedgerworks.com
      </li>
      <li>
        <svg viewBox="0 0 16 16" aria-hidden="true"><path d="M8 0a5.5 5.5 0 0 1 5.5 5.5C13.5 10 8 16 8 16S2.5 10 2.5 5.5A5.5 5.5 0 0 1 8 0zm0 3.5a2 2 0 1 0 0 4 2 2 0 0 0 0-4z"/></svg>
        418 W Larkspur Ave, Quarry Flats, AZ 85990
      </li>
    </ul>
  </section>

</main>
</body>
</html>
```